Wordpress Design Project

WHO WE ARE:
Bright Path Web Growth is not just another SEO or PPC company. We work with our clients to help them grow their business and achieve their goals. Our commitment to doing what is best for the customer, is why we have grown so quickly. We believe our business is not about advertising BUT about connecting customers & growing our clients businesses. We see our product as helping people, not selling a product.

PROJECT OVERVIEW:
I need to create a wordpress website for my business, www.brightpathwebgrowth.com.au

I need a whole new site created showing all of my services. The services include:
NOTE: These are not the main focus of the home page.

Consulting & Strategy Planning
Search Engine Optimisation
Pay Per Click
Re-Marketing

Once I have selected the top home page design, I will need a product and blog page designed.

SITE DESIGN:
If I was to explain the kind of style I am looking for, it would be high-street, New York agency look, web 2.0. Clean, elegant, stylish, high quality and simple looking. Kind of like you would expect from an quince website.

Think of car advertising, the closest to the target market & look/feel Im looking for would be Ravenmotor, Korel, Tamar, Brandin, Zepra.

However, I am open to any design style.

DO NOT let this restrict your creativity BUT here are some websites I like the look of.

Home page:
http://www.layoutfoundry.example/demo/52816.html
https://www.vantorix.example/intl/en/halo/devices/
http://www.vantorix.example/intl/en/halo/devices/features-different.html
http://www.layoutfoundry.example/demo/47190.html
https://www.vantorix.example/intl/en/halo/browser/features.html

Product Page:
http://www.vantorix.example/intl/en/halo/devices/buynow.html#instore

NOTE: I just added a file called "I like this color scheme.png" you can play around with something like this as well.
Updates

Please do not use the content from my current website. That is for a PPC service, the new site is for an full service agency.

Also, the message/tagline is the feature or most prominent element of the website..... Not the services we offer, these are secondary.

Great designs so far everyone, but I think I'm looking a little simpler and less crowded.  Closer to the sample sites I sent.... keep em coming.

Also, I would prefer that the 4 services, do not visually over power the tag line.  The 4 services are not important to the home page.

Lets make this easy, since every design I receive is almost the same...

Make the design look something like these 2 websites.
https://www.vantorix.example/intl/en/halo/browser/features.html#simplicity

Target Market(s)

Business Owners and entreprenuers who are well established, typically in the 35-60 year old range and spend 100k-1m in advertising per year. They big brands that target these people are Ravenmotor, Korel, Tamar, Brandin, Zepra, this should give you the feel for what I am after.

Industry/Entity Type

Advertising

Requirements
Must have
• 1. Navigations: Home, Services, About Us, Blog, Contact Us

2. The main home page words should be.... "We Grow Your Business Online" and "Clear Aim, Clear Plan, Clear Team, Bright Path Web Growth" (should use logo for last one)
I would like to see this tagline somewhere in the site "We Don't Want to be the Biggest, Just the Best!"

3. Product page must have a contact form with (name, email, phone, website)
This form must show an offer of "Free Strategy Sessions, Double your website leads", I have included an image to show as an example for the lead form "lead form example.png", see attached.

Nice to have
• I would like to see 1 or 2 of these idea's in the design.

1. I have attached some logos for Bidlane & Metricove certifications + Web association logo you can use for design purposes.

2. You can put company logo's in the design and I can change them to my clients logos at a later date.

3. Testimonials

4. Since our business is about people, pictures of people like business owners, customers using technology such as an slate, or anything like that would be good. However, is not necessary. Some idea: http://www.peerlattice.example/advertising
Should not have
• There will be no video on the design.

```html
<!DOCTYPE html>
<html lang="en">
<head>
<meta charset="utf-8">
<title>Bright Path Web Growth</title>
<link rel="stylesheet" href="https://fonts.googleapis.com/css2?family=Fredoka:wght@600&family=Play:wght@400;700&family=Questrial&family=Noto+Serif:ital@0;1&display=swap">
<style>
:root{
  --page:#ffffff;
  --ink:#1f1f1f;
  --muted:#555b61;
  --rule:#d9dde1;
  --brand-blue:#1c5fc0;
  --button-blue:#1f6fd8;
  --button-blue-dark:#1558b5;
  --sky-1:#67b2e6;
  --sky-2:#8cc6ea;
  --sky-3:#a9d5ee;
  --accent-orange:#f5831f;
  --band:#eef6fd;
  --band-line:#dbe8f4;
  --field-line:#c9ced3;
  --photo-a:#dfe9f4;
  --photo-b:#aac6e6;
  --map:#eef0f2;
  --social:#8e959c;
}
*{box-sizing:border-box;margin:0;padding:0}
html,body{width:983px;height:1200px;overflow:hidden}
body{position:relative;background:linear-gradient(#f4f5f6 0,#fff 140px);font-family:"Questrial",sans-serif;color:var(--ink)}
.abs{position:absolute}

/* header */
.brand{left:115px;top:22px;display:flex;align-items:center;gap:12px}
.brand-mark{width:52px;height:52px;border-radius:50%;background:var(--brand-blue)}
.brand-name{font-family:"Play",sans-serif;font-weight:700;font-size:22px;color:#3a3d41;line-height:1}
.share{top:18px;display:flex;height:16px;border:1px solid #c7cbd0;border-radius:3px;background:#f4f5f6;font:700 10px/14px "Play",sans-serif;color:#333;padding:0 6px}
.nav{top:50px;left:533px;font:700 11px/14px "Play",sans-serif;color:#555;letter-spacing:.3px}
.nav a{color:inherit;text-decoration:none;position:absolute;white-space:nowrap}
.nav .current{color:var(--brand-blue)}
.top-rule{left:115px;top:90px;width:752px;height:1px;background:var(--rule)}

/* hero */
.hero-photo{left:500px;top:110px;width:370px;height:390px;background:radial-gradient(ellipse at 60% 45%,var(--photo-b),var(--photo-a) 65%,rgba(255,255,255,0) 100%)}
.tagline{left:115px;top:131px;z-index:2;font-family:"Fredoka",sans-serif;font-weight:600;font-size:25px;line-height:31px;text-transform:uppercase;letter-spacing:0;white-space:nowrap}
.tagline span{display:block}
.tagline .l1{color:var(--sky-1)}
.tagline .l2{color:var(--sky-2)}
.tagline .l3{color:var(--sky-3)}
.tagline .l4{color:var(--accent-orange)}
.hero-copy{left:118px;top:277px;width:380px;font:italic 13px/21px "Noto Serif",serif;color:#2b2b2b}
.btn-primary{left:115px;top:366px;width:97px;height:27px;border-radius:3px;background:linear-gradient(var(--button-blue),var(--button-blue-dark));color:#fff;font:700 11.5px/27px "Play",sans-serif;text-align:center}
.slider-bar{left:115px;top:434px;width:385px;height:38px;border-radius:6px 0 0 6px;background:linear-gradient(90deg,#e6e7e8,#f2f3f4 70%,rgba(255,255,255,0))}
.dot{top:448px;width:10px;height:10px;border-radius:50%;background:#d3d5d7}
.dot.active{background:#3b3f44}
.arrows{left:207px;top:445px;font:12px/14px "Play",sans-serif;color:#777;letter-spacing:4px}

/* services */
.services{left:0;top:500px;width:983px;height:163px;background:var(--band);border-top:2px solid var(--band-line);border-bottom:2px solid var(--band-line)}
.service{top:520px;width:180px}
.service-head{display:flex;align-items:center;gap:8px;height:42px}
.service h3{font:700 14.5px/20px "Play",sans-serif;color:var(--brand-blue);white-space:nowrap}
.service p{margin-top:12px;width:160px;font-size:10.5px;line-height:14px;color:#222}
.service .more{display:block;margin-top:13px;font-weight:700;font-size:10.5px;color:#111}

/* testimonials */
.section-title{left:118px;top:690px;font:700 15px/20px "Play",sans-serif;color:#111}
.quote{top:733px;width:160px}
.quote-mark{position:absolute;left:-26px;top:-4px;font:700 30px/30px "Noto Serif",serif;color:#3f86d8}
.quote p{font:italic 9.5px/17px "Noto Serif",serif;color:#555;margin-bottom:17px}
.quote .author{position:absolute;top:192px;font:700 11.5px/14px "Play",sans-serif;color:#111}
.quote .site{position:absolute;top:210px;font:italic 10px/14px "Noto Serif",serif;color:#555;white-space:nowrap}

/* lead form */
.lead-box{left:649px;top:745px;width:199px;height:222px;border:1px solid #dde1e5;border-top:none;border-radius:0 0 4px 4px;background:#fff}
.ribbon{left:655px;top:703px}
.offer{left:681px;top:715px;font:700 11px/14px "Play",sans-serif;color:#fff;text-transform:uppercase;white-space:nowrap}
.badge{left:609px;top:693px;width:68px;height:68px;border-radius:50%;background:#1d7fd6;border:3px solid #fff;box-shadow:0 0 0 2px #1d7fd6;color:#fff;font:600 19px/62px "Fredoka",sans-serif;text-align:center;transform:rotate(-12deg)}
.field{left:661px;width:174px;height:28px;border:2px solid #e3e6e9;outline:1px solid var(--field-line);outline-offset:-3px;border-radius:3px;font:italic 10px/24px "Noto Serif",serif;color:#666;padding-left:9px;background:#fff}
.submit{left:660px;top:926px;width:75px;height:24px;border-radius:12px;background:linear-gradient(#f3fbff,#9fd6f6);border:1px solid #6cb8e6;font:700 italic 11px/22px "Noto Serif",serif;color:#123f6b;text-align:center}

/* footer */
.footer-rule{left:115px;top:1013px;width:752px;height:1px;background:var(--rule)}
.foot-head{top:1036px;font:700 9.5px/12px "Play",sans-serif;color:#111;text-transform:uppercase;letter-spacing:.3px}
.foot-list{top:1061px;font-size:10px;line-height:15.3px;color:#333;list-style:none}
.contact p{font-size:10px;line-height:15px;color:#333}
.world-map{left:288px;top:1040px;width:185px;height:95px;border-radius:40px;background:radial-gradient(ellipse,var(--map),rgba(255,255,255,0) 75%)}
.copyright{left:131px;top:1166px;font-size:10px;color:#333}
.social{top:1156px;width:11px;height:11px;border-radius:2px;background:var(--social)}
</style>
</head>
<body>

<header>
  <div class="abs brand"><span class="brand-mark"></span><span class="brand-name">Bright Path Web Growth</span></div>
  <div class="abs share" style="left:718px">Share</div>
  <div class="abs share" style="left:764px">Post</div>
  <div class="abs share" style="left:814px">Like&nbsp;0</div>
  <nav class="abs nav">
    <svg class="abs" style="left:0;top:0" width="12" height="11" viewBox="0 0 12 11"><path d="M6 0 0 5h2v6h3V7h2v4h3V5h2z" fill="#555"/></svg>
    <a class="current" style="left:40px" href="#">SERVICES</a>
    <a style="left:128px" href="#">ABOUT US</a>
    <a style="left:220px" href="#">BLOG</a>
    <a style="left:291px" href="#">CONTACT</a>
  </nav>
  <div class="abs top-rule"></div>
</header>

<section class="hero">
  <div class="abs hero-photo" role="img" aria-label="Photo of two smiling business people, a woman in a dark suit and a man in a light blue shirt and tie"></div>
  <h1 class="abs tagline">
    <span class="l1">We are not about advertising,</span>
    <span class="l2">we are about connecting</span>
    <span class="l3">your customers, and</span>
    <span class="l4">growing your business.</span>
  </h1>
  <p class="abs hero-copy">Lorem ipsum dolor sit amet consectetuer adipis cing elit. Praesent vestibulum molestie lacus. Aenean nonummy hendrerit mauris. Phasellus porta. Fusce sucipit varius mi.</p>
  <div class="abs btn-primary">Learn More &#8250;</div>
  <div class="abs slider-bar"></div>
  <span class="abs dot active" style="left:130px"></span>
  <span class="abs dot" style="left:145px"></span>
  <span class="abs dot" style="left:160px"></span>
  <span class="abs dot" style="left:175px"></span>
  <span class="abs arrows">&#8249;&#8250;</span>
</section>

<section class="abs services"></section>
<div class="abs service" style="left:115px">
  <div class="service-head">
    <svg width="34" height="38" viewBox="0 0 34 38"><circle cx="17" cy="9" r="8" fill="#333"/><path d="M2 38v-8c0-6 5-10 11-10h8c6 0 11 4 11 10v8z" fill="#333"/><path d="M17 21l-2 3 2 10 2-10z" fill="#eef6fd"/></svg>
    <h3>Consulting &amp;<br>Strategy Planning</h3>
  </div>
  <p>Magnis d patui entontessce iculu muss ceugiaead a odio. Mor unc avida cursus necucus.</p>
  <span class="more">Learn more...</span>
</div>
<div class="abs service" style="left:316px">
  <div class="service-head">
    <svg width="34" height="36" viewBox="0 0 34 36"><circle cx="20" cy="13" r="10" fill="none" stroke="#333" stroke-width="4"/><path d="M13 21 3 33" stroke="#333" stroke-width="6" stroke-linecap="round"/></svg>
    <h3>SEO</h3>
  </div>
  <p>Magnis d patui entontessce iculu muss ceugiaead a odio. Mor unc avida cursus necucus.</p>
  <span class="more">Learn more...</span>
</div>
<div class="abs service" style="left:517px">
  <div class="service-head">
    <svg width="32" height="36" viewBox="0 0 32 36"><path d="M10 2h4v14h2v-4h4v5h2v-3h4v5h2v-2h3v11c0 5-4 8-9 8h-6c-4 0-6-2-8-5L2 21l3-2 5 5z" fill="#333"/></svg>
    <h3>Pay Per Click</h3>
  </div>
  <p>Magnis d patui entontessce iculu muss ceugiaead a odio. Mor unc avida cursus necucus.</p>
  <span class="more">Learn more...</span>
</div>
<div class="abs service" style="left:717px">
  <div class="service-head">
    <svg width="32" height="36" viewBox="0 0 32 36"><path d="M2 2h20l8 8v24H2z" fill="none" stroke="#333" stroke-width="3"/><path d="M7 27l6-7 5 4 7-9" fill="none" stroke="#333" stroke-width="2.5"/></svg>
    <h3>Re-Marketing</h3>
  </div>
  <p>Magnis d patui entontessce iculu muss ceugiaead a odio. Mor unc avida cursus necucus.</p>
  <span class="more">Learn more...</span>
</div>

<section class="testimonials">
  <h2 class="abs section-title">What People Say:</h2>
  <blockquote class="abs quote" style="left:141px">
    <span class="quote-mark">&ldquo;</span>
    <p>Magnis d patui entontessce iculu muss ceugiaead a odio.</p>
    <p>Mor unc avida cursus necucus a lor isique ci ac sem ultricis pharmet erop sit amet consecueadi scineliris fere ntum dictum mag nadore aliqm leo telluo loapib ueleme ntum vel cnte eu lacusstib.</p>
    <span class="author">- Faucibus L</span>
    <span class="site">HTTP://websitename.com</span>
  </blockquote>
  <blockquote class="abs quote" style="left:389px">
    <span class="quote-mark">&ldquo;</span>
    <p>Magnis d patui entontessce iculu muss ceugiaead a odio.</p>
    <p>Mor unc avida cursus necucus a lor isique ci ac sem ultricis pharmet erop sit amet consecueadi scineliris fere ntum dictum mag nadore aliqm leo telluo loapib ueleme ntum vel cnte eu lacusstib.</p>
    <span class="author">- Faucibus L</span>
    <span class="site">HTTP://websitename.com</span>
  </blockquote>
</section>

<section class="lead-form">
  <div class="abs lead-box"></div>
  <svg class="abs ribbon" width="212" height="48" viewBox="0 0 212 48"><defs><linearGradient id="ribbonFill" x1="0" y1="0" x2="0" y2="1"><stop offset="0" stop-color="#fb9a2a"/><stop offset="1" stop-color="#e4650d"/></linearGradient></defs><path d="M0 0h196l16 24-16 24H0z" fill="url(#ribbonFill)"/></svg>
  <div class="abs offer">Strategy sessions,<br>double your website leads</div>
  <div class="abs badge">FREE</div>
  <div class="abs field" style="top:763px">Full Name:</div>
  <div class="abs field" style="top:801px">Enter Email:</div>
  <div class="abs field" style="top:840px">Phone:</div>
  <div class="abs field" style="top:878px">Website:</div>
  <div class="abs submit">Submit &raquo;</div>
</section>

<footer>
  <div class="abs footer-rule"></div>
  <h4 class="abs foot-head" style="left:131px">Contact Information</h4>
  <div class="abs contact" style="left:131px;top:1061px">
    <p>4120 Larkfield Lane Dunmore,<br>K07 52TX</p>
    <p style="margin-top:8px">Phone: +1 800 555 01927<br>E-mail: hello@brightpathmail.example</p>
  </div>
  <div class="abs world-map" role="img" aria-label="Faint dotted world map"></div>
  <h4 class="abs foot-head" style="left:565px">Quick Links</h4>
  <ul class="abs foot-list" style="left:565px"><li>Home</li><li>Services</li><li>About Us</li><li>Blog</li></ul>
  <h4 class="abs foot-head" style="left:709px">Our Services</h4>
  <ul class="abs foot-list" style="left:709px"><li>Consulting &amp; Strategy Planning</li><li>Search Engine Optimisation</li><li>Pay Per Click</li><li>Re-Marketing</li></ul>
  <p class="abs copyright">Copyright &copy; 2012 &nbsp;Bright Path Web Growth, &nbsp;All rights reserved</p>
  <span class="abs social" style="left:712px;background:#2f5fa8"></span>
  <span class="abs social" style="left:731px"></span>
  <span class="abs social" style="left:749px"></span>
  <span class="abs social" style="left:767px"></span>
</footer>

</body>
</html>
```